Harlow Mailbox Services, full-service collaboration with postal service - installation of units

1. CBU - Cluster Box Unit - These are Mailbox units that you would see at residential neighborhoods, and Apartments -
2. Logo Needed
3. Maybe have CBU as a division of DWFS (Dermot Vance Field Services)
4. Card to be primary Harlow Mailbox Services

This is a letter of introduction that I am developing:

I am writing to introduce Dermot Vance Field Services, a company dedicated to delivering exceptional service and quality in the installation and maintenance of commercial mailboxes, specifically Cluster Box Units (CBUs). Our commitment to excellence and customer satisfaction has established us as a trusted partner for developers and postal services alike.
At Dermot Vance Field Services, we take pride in our comprehensive approach, ensuring that every step of the mailbox installation process is handled with precision and care. Our services include:
• Supplying high-quality CBUs tailored to meet the specific needs of your development.
• Providing a CBU plat layout upon approval of the address plat, ensuring seamless integration into your development plans.
• Collaborating with developers and postmasters to determine the optimal CBU locations for efficient mail delivery.
• Qualifying the labeling of CBU units, offering both sticker and etching options to suit your preferences.
• Pouring durable concrete foundations as required for the secure installation of the CBU units.
• Handling the installation process with expertise and attention to detail.
• Labeling the units and supplying keys for each mailbox, ensuring a smooth transition for residents and businesses.
Our team is dedicated to working closely with you to ensure that all requirements are met and that the installation process is completed efficiently and to the highest standards.
We look forward to the opportunity to collaborate with you and contribute to the success of your project. Please do not hesitate to contact us for any additional information or to discuss your specific requirements.
Sincerely,
Dermot Vance
Dermot Vance Field Services

Target Market(s)

Developers, Builders, Apartment's, HOA

Industry/Entity Type

Construction

Contact Information for Business Card

Name: Dermot Vance, Cell:555-671-0148, Email: derm@dvfieldco.example

Font styles to use
Serif

Requirements
Must have
• Fresh Looking
Nice to have
• Maybe a CBU Box if it looks clean
Should not have
• Not Industrial or Old traditional card

```html
<!DOCTYPE html>
<html lang="en">
<head>
<meta charset="utf-8">
<title>Harlow Mailbox Services – Business Card</title>
<link rel="stylesheet" href="https://fonts.googleapis.com/css2?family=Roboto+Slab:wght@400;600;700&display=swap">
<style>
  :root {
    --brand-red: #82152b;
    --card-white: #ffffff;
    --backdrop: #b3b3b3;
  }
  * { margin: 0; padding: 0; box-sizing: border-box; }
  html, body {
    width: 1200px; height: 1200px; overflow: hidden;
    background: var(--backdrop);
    font-family: "Roboto Slab", serif;
  }
  .canvas { position: relative; width: 1200px; height: 1200px; }
  .card {
    position: absolute; left: 154px; width: 891px; height: 522px;
    background: var(--card-white); overflow: hidden;
  }
  .card--front { top: 56px; }
  .card--back { top: 621px; }
  .card__shapes { position: absolute; inset: 0; width: 100%; height: 100%; }
  .wordmark { position: absolute; color: var(--brand-red); font-weight: 600; line-height: 1.1; }
  .wordmark__name { display: block; letter-spacing: 0.01em; }
  .wordmark__sub { display: block; letter-spacing: 0.12em; }
  .card--front .wordmark { left: 62px; top: 218px; }
  .card--front .wordmark__name { font-size: 31px; }
  .card--front .wordmark__sub { font-size: 17px; margin-top: 6px; }
  .card--back .wordmark { left: 0; right: 0; top: 140px; text-align: center; }
  .card--back .wordmark__name { font-size: 58px; }
  .card--back .wordmark__sub { font-size: 29px; margin-top: 8px; }
  .contact-name {
    position: absolute; left: 446px; right: 0; top: 108px;
    text-align: center; color: var(--card-white);
    font-size: 36px; font-weight: 700;
  }
  .contact-line {
    position: absolute; left: 574px; color: var(--card-white);
    font-size: 20px; font-weight: 400; letter-spacing: 0.02em;
  }
  .contact-line--phone { top: 298px; }
  .contact-line--email { top: 408px; }
</style>
</head>
<body>
<main class="canvas">
  <section class="card card--front">
    <svg class="card__shapes" viewBox="0 0 891 522" aria-hidden="true">
      <rect class="contact-panel" x="446" y="0" width="445" height="522" fill="var(--brand-red)"/>
      <polygon class="panel-notch" points="446,212 554,262 554,522 446,522" fill="var(--card-white)"/>
      <polygon class="icon-tile" points="446,240 542,284 542,345 446,333" fill="var(--brand-red)"/>
      <polygon class="icon-tile" points="446,350 542,394 542,483 446,446" fill="var(--brand-red)"/>
      <path class="icon-phone" fill="var(--card-white)" transform="translate(480,296) scale(1.15)"
        d="M6.6 10.8c1.4 2.8 3.8 5.1 6.6 6.6l2.2-2.2c.3-.3.7-.4 1-.2 1.1.4 2.3.6 3.6.6.6 0 1 .4 1 1V20c0 .6-.4 1-1 1C10.6 21 3 13.4 3 4c0-.6.4-1 1-1h3.5c.6 0 1 .4 1 1 0 1.3.2 2.5.6 3.6.1.3 0 .7-.2 1L6.6 10.8z"/>
      <g class="icon-mail" transform="translate(480,402)">
        <rect x="0" y="0" width="28" height="20" rx="2" fill="var(--card-white)"/>
        <polyline points="2,3 14,12 26,3" fill="none" stroke="var(--brand-red)" stroke-width="2.2"/>
      </g>
    </svg>
    <div class="wordmark">
      <span class="wordmark__name">HARLOW MAILBOX</span>
      <span class="wordmark__sub">Services, LLC</span>
    </div>
    <h1 class="contact-name">Dermot Vance</h1>
    <p class="contact-line contact-line--phone">555-671-0148</p>
    <p class="contact-line contact-line--email">derm@dvfieldco.example</p>
  </section>

  <section class="card card--back">
    <svg class="card__shapes" viewBox="0 0 891 522" aria-hidden="true">
      <polygon class="corner-band" points="0,454 290,454 325,398 718,398 891,237 891,522 0,522" fill="var(--brand-red)"/>
    </svg>
    <div class="wordmark">
      <span class="wordmark__name">HARLOW MAILBOX</span>
      <span class="wordmark__sub">Services, LLC</span>
    </div>
  </section>
</main>
</body>
</html>
```